Creative Web Designer: Refresh & Elevate our Beach Lifestyle Brand with a Joyful, Elegant Red...

Corallune (corallune.gr), a vibrant Greek brand celebrated for its high-quality beachwear and accessories, is embarking on an exciting phase as we enter our third year. Renowned for our stylish flip flops, beach towels, and caps, we are thrilled to announce the expansion of our product line with innovative beach essentials and a fresh palette for our existing collection.
As we continue to grow and evolve, we are in search of a talented and imaginative web designer who can capture the essence of Corallune and translate it into a digital experience. Our ideal candidate will craft a website that mirrors the happiness and relaxation of a day at the beach, while also embodying the sophistication and elegance that our brand represents.
Your Mission:
Design a Website That Reflects Our Brand Identity: Create a website that is visually stunning, easy to navigate, and showcases our products in a way that feels both refreshing and luxurious.
Incorporate New Product Lines and Colors: Seamlessly integrate our new beach products and color schemes, ensuring the website remains cohesive and on-brand.
User Experience is Key: Design a user-friendly interface that ensures a seamless shopping experience for our customers, with intuitive navigation and a mobile-responsive design.
Embrace Creativity While Staying Elegant: We want our website to be a reflection of the joy and elegance that our products bring to our customers. Your design should be innovative, incorporating modern web design trends that align with our brand's aesthetic.
What We're Looking For:
A portfolio that demonstrates experience in creating visually appealing and user-friendly e-commerce websites.
Strong understanding of branding and the ability to translate a brand's essence into a digital format.
Proficiency in the latest web design software and technologies.
Excellent communication skills and the ability to work collaboratively with our team to bring our vision to life.
This is a fantastic opportunity for a web designer who loves the beach lifestyle and is passionate about creating beautiful, effective websites. If you're ready to dive into a project that will challenge and excite you, while making a significant impact on our growing brand, we would love to hear from you.
Regarding the products, on the website (corallune.gr) you will the flips flops and on the attached powerpoint all the accessories for this summer. Please use the images to craft your designs.
Join us in making Corallune the go-to brand for beach enthusiasts everywhere. Apply now to start the conversation and share your vision for our new website 😊🩴☀️⛱️
p.s. we didn;t mention the pages to be designed. Its 4 pages in all,
homepage, product category page, singleproduct page and contact us page

```html
<!DOCTYPE html>
<html lang="en">
<head>
<meta charset="utf-8">
<title>Corallune – Landing Page Mobile View</title>
<link href="https://fonts.googleapis.com/css2?family=Inter:wght@400;500;600;700&family=Poppins:wght@700;800&display=swap" rel="stylesheet">
<style>
:root{
  --bg:#f2f2f2;
  --navy:#1d1b4f;
  --blue:#35b8f0;
  --blue-deep:#1e9fe6;
  --violet:#7d8ef0;
  --grey:#6b7280;
  --line:#e6eaf0;
  --soft:#eef5fc;
  --white:#ffffff;
  --yellow:#f6d21c;
}
*{box-sizing:border-box;margin:0;padding:0}
html,body{width:1115px;height:1200px;overflow:hidden;background:var(--bg);font-family:"Inter",sans-serif;color:var(--navy)}
.board{position:relative;width:1115px;height:1200px}
.abs{position:absolute}
.brand{left:108px;top:196px;font-family:"Inter",sans-serif;font-weight:700;font-size:40px;color:var(--navy);letter-spacing:1px}
.headline{left:103px;top:322px;font-family:"Poppins",sans-serif;font-weight:800;font-size:47px;line-height:56px;color:var(--blue)}
.panel{position:absolute;overflow:hidden;border-radius:8px;background:var(--white)}
.pill{position:absolute;border-radius:20px;background:var(--soft);color:var(--blue);font-weight:500;display:flex;align-items:center;justify-content:center}
.photo{position:absolute;border-radius:8px}
.circle{position:absolute;border-radius:50%}
.t{position:absolute;white-space:nowrap}
/* hero */
.hero{left:592px;top:0;width:208px;height:260px;background:linear-gradient(180deg,#eaf3fb,#f8fbff)}
.hero h1{position:absolute;left:10px;top:46px;font-size:15.5px;line-height:19px;font-weight:700;letter-spacing:-.3px;color:var(--navy)}
.hero h1 span{color:var(--blue)}
.btn-primary{position:absolute;border-radius:4px;background:var(--blue);color:var(--white);font-weight:600;display:flex;align-items:center;justify-content:center;box-shadow:0 4px 10px rgba(53,184,240,.35)}
.note-card{position:absolute;background:var(--white);border-radius:6px;box-shadow:0 4px 14px rgba(30,60,120,.08)}
/* why */
.why{left:588px;top:300px;width:207px;height:446px}
.feature{position:absolute;left:10px;width:186px;height:54px;border-radius:4px}
.feature.raised{background:var(--white);box-shadow:0 3px 10px rgba(30,60,120,.1)}
.feature .ico{position:absolute;left:10px;top:16px;width:20px;height:20px;border-radius:4px}
.feature b{position:absolute;left:38px;top:10px;font-size:8px;font-weight:600}
.feature p{position:absolute;left:38px;top:22px;width:140px;font-size:7px;line-height:9.5px;color:var(--grey)}
/* product */
.product{left:594px;top:818px;width:205px;height:382px;border-radius:8px 8px 0 0}
.product .band{position:absolute;left:0;top:10px;width:205px;height:326px;background:linear-gradient(180deg,#3bbaf3 0%,#4aa8f2 60%,#7b8ff0 100%)}
.card{position:absolute;background:var(--white);border-radius:8px}
.nav-dot{position:absolute;width:14px;height:14px;border-radius:50%;display:flex;align-items:center;justify-content:center}
/* faq */
.faq{left:861px;top:68px;width:208px;height:434px;background:linear-gradient(180deg,#fff 0%,#fff 56%,#eef2fb 80%,#f3f6fc 100%)}
.row{position:absolute;left:2px;width:204px;border-bottom:1px solid var(--line);font-size:7px;font-weight:600;line-height:11px;color:var(--navy)}
.chev{position:absolute;right:16px;width:14px;height:14px;border-radius:50%;border:1px solid #d5dae2;background:var(--white)}
.chev svg{position:absolute;left:3px;top:3px}
/* newsletter */
.news{left:854px;top:610px;width:206px;height:430px;background:linear-gradient(180deg,#3bbaf3,#52b4f5)}
.news .top{position:absolute;left:6px;top:0;width:194px;height:156px;background:var(--white);border-radius:0 0 10px 10px}
.outline-btn{position:absolute;border-radius:3px;font-size:10px;font-weight:500;display:flex;align-items:center;justify-content:center}
.footer-t{position:absolute;left:0;width:206px;text-align:center;color:var(--white);font-size:10px}
</style>
</head>
<body>
<div class="board">

  <div class="abs brand">Corallune</div>
  <div class="abs headline">Landing Page<br>Mobile View</div>

  <!-- Hero screen -->
  <section class="panel hero">
    <div class="pill" style="left:10px;top:-2px;width:58px;height:10px;background:#fff;font-size:3px;color:var(--grey)">Comfort with your summer outfit</div>
    <div class="pill" style="left:10px;top:18px;width:90px;height:26px;background:#fff;font-size:7px">#saltytimes</div>
    <h1>Innovative Natural Rubber<br><span>Beach</span> Accessories</h1>
    <div class="t" style="left:10px;top:89px;font-size:6.6px;color:var(--grey)">Our Greek and sustainable answer for summer flip flops.</div>
    <div class="btn-primary" style="left:10px;top:121px;width:78px;height:29px;font-size:8px">Start Now →</div>
    <div class="circle" style="left:99px;top:123px;width:24px;height:24px;background:#fff;border:1px solid #cfe9fb">
      <svg width="24" height="24" viewBox="0 0 24 24"><path d="M10 8.5l5 3.5-5 3.5z" fill="#35b8f0"/></svg>
    </div>
    <div class="t" style="left:127px;top:131px;font-size:7.5px;color:#3a3f55;font-weight:500">Watch Our Product</div>
    <div class="circle" style="left:48px;top:168px;width:7px;height:7px;background:#d6d9df"></div>
    <div class="circle" style="left:10px;top:177px;width:30px;height:30px;background:var(--blue)"></div>
    <div class="note-card" style="left:25px;top:182px;width:143px;height:80px">
      <div class="pill" style="left:11px;top:13px;width:54px;height:14px;font-size:5.5px">#FeelTheSun</div>
      <div class="t" style="left:11px;top:40px;font-size:10px;line-height:15px;color:#3a3f55;white-space:normal;width:125px">We are your best choice for accessories!</div>
    </div>
    <div class="circle" style="left:144px;top:176px;width:18px;height:18px;background:#fff;box-shadow:0 2px 6px rgba(0,0,0,.08)"></div>
    <div class="circle" style="left:160px;top:188px;width:20px;height:20px;background:#fff;box-shadow:0 2px 6px rgba(0,0,0,.08)"></div>
  </section>

  <!-- Why choose us screen -->
  <section class="panel why">
    <div class="photo" role="img" aria-label="Woman holding a yellow flip-flop by the harbour" style="left:36px;top:5px;width:141px;height:80px;background:linear-gradient(135deg,#3f5a54,#c9a26a 50%,#e8c64a 70%,#6f8aa6)"></div>
    <div class="note-card" style="left:83px;top:68px;width:113px;height:37px">
      <div class="t" style="left:37px;top:10px;font-size:6px;line-height:9px;color:var(--blue);white-space:normal;width:70px">Comfort on your own with extra durability</div>
    </div>
    <div class="circle" style="left:185px;top:19px;width:5px;height:5px;background:var(--navy)"></div>
    <div class="circle" style="left:22px;top:104px;width:6px;height:6px;background:var(--yellow)"></div>
    <div class="t" style="left:10px;top:126px;font-size:19px;font-weight:700;color:var(--blue)">Why Choose Us</div>
    <div class="t" style="left:10px;top:158px;font-size:7px;line-height:10px;white-space:normal;width:180px;color:#2b2f45">Enjoy unforgetable experience wearing <span style="color:var(--blue);font-weight:600">#Corallune</span> accesories for your comfort!</div>
    <div class="feature raised" style="top:190px">
      <div class="ico" role="img" aria-label="Green sprout icon" style="background:#7dc24b"></div>
      <b>100% Natural Rubber</b><p>Vitae donec pellentesque a aliquam et ultricies auctor.</p>
    </div>
    <div class="feature" style="top:248px">
      <div class="ico" role="img" aria-label="Teal flip-flop icon" style="background:#4fb4b0"></div>
      <b>Best Durability</b><p>Vitae donec pellentesque a aliquam et ultricies auctor.</p>
    </div>
    <div class="feature" style="top:300px">
      <div class="ico" role="img" aria-label="Camera icon" style="background:#4a4f5a"></div>
      <b>Comfort with Perfect Cuts!</b><p>Vitae donec pellentesque a aliquam et ultricies auctor.</p>
    </div>
    <div class="t" style="left:25px;top:360px;font-size:10px;font-weight:500">See Product &nbsp;›</div>
    <div class="photo" role="img" aria-label="Couple in patterned shirts in front of a camper van" style="left:28px;top:410px;width:158px;height:40px;border-radius:14px 14px 0 0;background:linear-gradient(180deg,#9fbcd4,#4d6a86 60%,#2f4058)"></div>
  </section>

  <!-- Product screen -->
  <section class="panel product">
    <div class="band"></div>
    <div class="photo" role="img" aria-label="Couple beside a vintage camper van on the beach" style="left:27px;top:2px;width:158px;height:52px;border-radius:0 0 10px 10px;background:linear-gradient(135deg,#6f93a8,#d8c6a6 50%,#3a5a7a)"></div>
    <div class="circle" style="left:82px;top:14px;width:14px;height:14px;background:rgba(255,255,255,.9)"></div>
    <div class="circle" style="left:174px;top:44px;width:18px;height:18px;background:rgba(255,255,255,.35)"></div>
    <div class="t" style="left:8px;top:101px;font-size:7.5px;font-weight:600;color:#fff;letter-spacing:1px">OUR PRODUCT</div>
    <div class="t" style="left:8px;top:115px;font-size:8px;font-weight:600;color:#fff">
      <svg width="12" height="12" viewBox="0 0 12 12" style="vertical-align:middle;margin-right:4px"><rect x="1.5" y="3.5" width="9" height="7" rx="1" fill="none" stroke="#fff"/><path d="M4 3.5V2h4v1.5" fill="none" stroke="#fff"/></svg>• Choose Your Favourite!</div>
    <div class="t" style="left:162px;top:112px;font-size:6.5px;color:#fff">See All &nbsp;›</div>
    <div class="nav-dot" style="left:159px;top:143px;background:rgba(255,255,255,.25)"><svg width="8" height="8" viewBox="0 0 8 8"><path d="M6.5 4h-5M3.5 2L1.5 4l2 2" fill="none" stroke="#fff"/></svg></div>
    <div class="nav-dot" style="left:183px;top:143px;background:var(--navy)"><svg width="8" height="8" viewBox="0 0 8 8"><path d="M1.5 4h5M4.5 2l2 2-2 2" fill="none" stroke="#fff"/></svg></div>
    <div class="card" style="left:8px;top:157px;width:128px;height:148px">
      <div class="pill" style="left:11px;top:12px;width:52px;height:16px;font-size:5.5px">#FlipFlop</div>
      <div class="t" style="left:11px;top:38px;font-size:9.5px;color:#3a3f55">Aqua Flip-Flop</div>
      <div role="img" aria-label="Pair of grey-blue flip-flops" style="position:absolute;left:9px;top:53px;width:111px;height:77px;border:1px solid var(--line);border-radius:8px;background:radial-gradient(ellipse at 50% 50%,#9fb0c6 0%,#c9d3e0 40%,#fff 70%)"></div>
    </div>
    <div class="circle" style="left:120px;top:150px;width:20px;height:20px;background:#fff;border:1px solid #fbe9a3"></div>
    <div class="card" style="left:151px;top:157px;width:128px;height:148px">
      <div class="pill" style="left:11px;top:12px;width:52px;height:16px;font-size:5.5px">#Totebag</div>
      <div class="t" style="left:11px;top:38px;font-size:9.5px;color:#3a3f55">Beach Tote</div>
      <div role="img" aria-label="Black beach tote bag" style="position:absolute;left:9px;top:53px;width:111px;height:77px;border:1px solid var(--line);border-radius:8px;background:linear-gradient(90deg,#fff 60%,#2a2d33 75%)"></div>
    </div>
    <div class="t" style="left:8px;top:364px;font-size:7.5px;font-weight:600;color:var(--blue);letter-spacing:1px">FREQUENTLY ASKED QUESTION</div>
  </section>

  <!-- FAQ & testimonials screen -->
  <section class="panel faq">
    <div class="row" style="top:5px;height:33px;padding:11px 0 0 10px">Lorem Ipsum is simply dummy text?<span class="chev" style="top:10px"><svg width="8" height="8"><path d="M3 1.5l2.5 2.5L3 6.5" fill="none" stroke="#555"/></svg></span></div>
    <div class="row" style="top:38px;height:79px;background:#f2f5f9;padding:12px 0 0 12px;color:var(--blue);font-size:8px">Lorem Ipsum is simply dummy?
      <span class="chev" style="top:9px;background:var(--blue-deep);border:none"><svg width="8" height="8"><path d="M1.5 5.5L4 3l2.5 2.5" fill="none" stroke="#fff"/></svg></span>
      <span style="position:absolute;left:15px;top:38px;width:150px;white-space:normal;font-size:7px;line-height:12.5px;font-weight:500;color:var(--navy)">Lorem Ipsum is simply dummy text of the printing and typesetting industry. Lorem Ipsum has been the industry's standard</span>
    </div>
    <div class="row" style="top:117px;height:32px;padding:4px 40px 0 13px;white-space:normal">Printing and typesetting industry. Lorem Ipsum has been the industry's standard?<span class="chev" style="top:9px"><svg width="8" height="8"><path d="M3 1.5l2.5 2.5L3 6.5" fill="none" stroke="#555"/></svg></span></div>
    <div class="row" style="top:149px;height:33px;padding:5px 40px 0 13px;white-space:normal">Lorem Ipsum has been the industry's standard dummy text ever since the 1500s<span class="chev" style="top:10px"><svg width="8" height="8"><path d="M3 1.5l2.5 2.5L3 6.5" fill="none" stroke="#555"/></svg></span></div>
    <div class="t" style="left:0;width:208px;text-align:center;top:228px;font-size:10px;font-weight:500;color:var(--blue)">Let’s Hear</div>
    <div class="t" style="left:0;width:208px;text-align:center;top:243px;font-size:10px;font-weight:600">What They Says</div>
    <div class="t" style="left:12px;top:266px;font-size:26px;font-weight:700;color:var(--blue)">“</div>
    <div class="t" style="left:180px;top:266px;font-size:26px;font-weight:700;color:var(--blue)">”</div>
    <div class="t" style="left:33px;top:278px;width:142px;white-space:normal;text-align:center;font-size:6.8px;line-height:8.8px;color:var(--grey)">Lorem ipsum dolor sit amet, consectetur adipiscing elit. Risus vel lobortis tincidunt fames quisque mauris at diam. Nullam morbi ipsum turpis amet id posuere torto quis nostrud exercitation ullamco laboris nisi ut aliquip ex ea commodo consequat.</div>
    <div class="circle" role="img" aria-label="Client portrait" style="left:30px;top:360px;width:12px;height:12px;background:#9aa3ad"></div>
    <div class="circle" role="img" aria-label="Client portrait" style="left:62px;top:358px;width:15px;height:15px;background:#8a8f96"></div>
    <div class="circle" role="img" aria-label="Featured client portrait" style="left:92px;top:353px;width:24px;height:24px;background:#b5714f;border:2px solid var(--yellow)"></div>
    <div class="circle" role="img" aria-label="Client portrait" style="left:132px;top:358px;width:15px;height:15px;background:#7c838c"></div>
    <div class="circle" role="img" aria-label="Client portrait" style="left:166px;top:360px;width:12px;height:12px;background:#6fbf9a"></div>
    <div class="t" style="left:0;width:208px;text-align:center;top:380px;font-size:6px;font-weight:600">Lorem Ipsum</div>
    <div class="t" style="left:0;width:208px;text-align:center;top:391px;font-size:5.5px;color:var(--grey)">Our Client</div>
  </section>

  <!-- Newsletter & footer screen -->
  <section class="panel news">
    <div class="top">
      <div class="circle" style="left:-16px;top:-20px;width:46px;height:46px;background:#bfe6fb"></div>
      <div class="circle" style="left:164px;top:-20px;width:46px;height:46px;background:#bfe6fb"></div>
      <div class="t" style="left:0;width:194px;text-align:center;top:22px;font-size:10.5px;font-weight:600">How We Can Help You</div>
      <div class="t" style="left:14px;width:166px;white-space:normal;text-align:center;top:37px;font-size:6.5px;line-height:10px;color:#3a3f55">Follow our newsletter. We will regulary update our latest project and availability.</div>
      <div style="position:absolute;left:11px;top:78px;width:172px;height:35px;background:#eef3f9;border-radius:4px">
        <svg width="12" height="9" viewBox="0 0 12 9" style="position:absolute;left:10px;top:13px"><rect width="12" height="9" rx="1" fill="#4b5268"/><path d="M0.5 1l5.5 4 5.5-4" fill="none" stroke="#eef3f9"/></svg>
        <div class="t" style="left:27px;top:14px;font-size:5.5px;color:var(--grey)">Enter your email address</div>
        <div class="btn-primary" style="left:109px;top:6px;width:59px;height:22px;font-size:9px;font-weight:500;box-shadow:none">Subscribe</div>
      </div>
    </div>
    <div style="position:absolute;left:6px;top:180px;width:192px;height:96px;border:2px solid rgba(255,255,255,.85);border-radius:6px;background:rgba(255,255,255,.08)">
      <div class="t" style="left:10px;top:18px;font-size:6.5px;color:var(--navy)">Be The Next You with Corallune</div>
      <div class="t" style="left:10px;top:30px;width:170px;white-space:normal;font-size:10px;line-height:14.5px;font-weight:700;color:var(--navy)">Innovative Natural Rubber Beach Accessories</div>
      <div class="outline-btn" style="left:10px;top:63px;width:72px;height:20px;background:#fff;color:var(--blue)">Sign In</div>
      <div class="outline-btn" style="left:110px;top:63px;width:72px;height:20px;background:#9fdcf9;color:#fff;border:1px solid #fff">Sign Up</div>
    </div>
    <div class="t" style="left:14px;top:283px;font-size:14px;font-weight:700;color:var(--navy)">Corallune</div>
    <div class="t" style="left:10px;top:310px;font-size:10px;color:#fff;word-spacing:9px">Shop About Contact</div>
    <div style="position:absolute;left:50px;top:325px;width:82px;height:1px;background:rgba(255,255,255,.7)"></div>
    <div class="circle" style="left:11px;top:333px;width:9px;height:9px;border:1px solid #fff"></div>
    <div class="circle" style="left:30px;top:333px;width:9px;height:9px;border:1px solid #fff"></div>
    <div class="circle" style="left:49px;top:333px;width:9px;height:9px;border:1px solid #fff"></div>
    <div class="circle" style="left:68px;top:333px;width:9px;height:9px;border:1px solid #fff"></div>
    <div class="circle" style="left:130px;top:250px;width:150px;height:150px;border:22px solid rgba(255,255,255,.08)"></div>
    <div class="footer-t" style="top:366px">Terms of Use | Privacy Policy</div>
    <div class="footer-t" style="top:380px">Payment Methods | Refund Policy</div>
    <div class="footer-t" style="top:414px">© 2024 | Corallune</div>
  </section>

</div>
</body>
</html>
```